Tin Lantern Photo Booths

Im in need of business cards with a logo for my new Photo Booth business. The company will be called: Tin Lanterns Photo Booth.

Website: www.tinlanternphotobooths.example
Phone#: 555.274.0619
Bullet Points: Weddings, Charity Events, Private Parties, Corporate Parties,

Please make the logo fun. I like a clean look that and something that is very attention grabbing.

The photo booth will be setup for customers to come inside and have their pictures taken.

Good luck and have fun with it.

```html
<!DOCTYPE html>
<html lang="en">
<head>
<meta charset="utf-8">
<title>Tin Lanterns Photo Booth – Business Card</title>
<link href="https://fonts.googleapis.com/css2?family=PT+Sans:wght@400;700&display=swap" rel="stylesheet">
<style>
  :root {
    --page: #ffffff;
    --card: #ffffff;
    --ink: #111111;
    --accent: #8dc63f;
    --mark: #8a8a8a;
    --shadow: rgba(0, 0, 0, 0.38);
  }
  * { box-sizing: border-box; margin: 0; padding: 0; }
  html, body {
    width: 1200px;
    height: 900px;
    overflow: hidden;
    background: var(--page);
    font-family: "PT Sans", Tahoma, sans-serif;
    color: var(--ink);
  }
  .sheet { position: relative; width: 1200px; height: 900px; }
  .card {
    position: absolute;
    top: 246px;
    width: 514px;
    height: 314px;
    background: var(--card);
    box-shadow: 4px 6px 7px var(--shadow);
    border: 1px solid #eeeeee;
  }
  .card--front { left: 79px; }
  .card--back { left: 641px; }
  .side-label {
    position: absolute;
    top: 606px;
    font-size: 24px;
    font-weight: 400;
  }
  .side-label--front { left: 90px; }
  .side-label--back { left: 657px; }

  .brand { position: absolute; display: flex; align-items: center; }
  .brand__words { display: flex; flex-direction: column; line-height: 1; font-weight: 400; color: var(--ink); }
  .brand__dot { border-radius: 50%; background: var(--mark); flex: none; }

  .card--front .brand { left: 36px; top: 124px; gap: 16px; }
  .card--front .brand__name { font-size: 50px; letter-spacing: 1px; text-transform: uppercase; }
  .card--front .brand__tag { font-size: 27px; text-transform: uppercase; margin-top: 4px; }
  .card--front .brand__dot { width: 62px; height: 62px; }

  .card--back .brand { left: 24px; top: 34px; gap: 9px; }
  .card--back .brand__name { font-size: 28px; letter-spacing: 1px; text-transform: uppercase; }
  .card--back .brand__tag { font-size: 15px; text-transform: uppercase; margin-top: 3px; }
  .card--back .brand__dot { width: 34px; height: 34px; }

  .contact {
    position: absolute;
    left: 0;
    right: 0;
    top: 186px;
    text-align: center;
    padding-left: 30px;
  }
  .contact__phone { font-size: 27px; line-height: 1.1; }
  .contact__web { font-size: 19px; margin-top: 12px; }
  .services {
    list-style: none;
    display: flex;
    justify-content: center;
    margin-top: 20px;
    font-size: 15.5px;
  }
  .services li + li::before {
    content: "|";
    color: var(--accent);
    margin: 0 6px;
  }
</style>
</head>
<body>
  <main class="sheet">
    <section class="card card--front" aria-label="Card front">
      <div class="brand">
        <div class="brand__words">
          <span class="brand__name">Tin Lanterns</span>
          <span class="brand__tag">Photo Booth</span>
        </div>
        <span class="brand__dot" aria-hidden="true"></span>
      </div>
    </section>
    <p class="side-label side-label--front">Front</p>

    <section class="card card--back" aria-label="Card back">
      <div class="brand">
        <div class="brand__words">
          <span class="brand__name">Tin Lanterns</span>
          <span class="brand__tag">Photo Booth</span>
        </div>
        <span class="brand__dot" aria-hidden="true"></span>
      </div>
      <div class="contact">
        <p class="contact__phone">Contact - 555.274.0619</p>
        <p class="contact__web">www.tinlanternphotobooths.example</p>
        <ul class="services">
          <li>Weddings</li>
          <li>Charity Events</li>
          <li>Private Parties</li>
          <li>Corporate Parties</li>
        </ul>
      </div>
    </section>
    <p class="side-label side-label--back">Back</p>
  </main>
</body>
</html>
```